Flyer for Luxury Boarding Stable for Retired Horses

A one page flyer to hand out at stable tours and at horse shows. Quiet Meadows at 41 Acres is a luxury equine boarding stable for retired horses. This is a new facility in Summerfield, NC that has 6 available stalls. We are trying to attract owners with 2 or more retired horses they would like to board.

Target Market(s)

Horse owners with 2 or more horses that are retired from showing, racing, or rodeo. These owners love their horses like family and want them well cared for in their retirement years.

Industry/Entity Type

Equestrian Boarding

Font styles to use
Script

Colors
EE7325
F08F49
F5BC92
FAE3D3
FDF4ED

Requirements
Must have
• Photos of the facility. Must feel upscale and worth the price.

```html
<!DOCTYPE html>
<html lang="en">
<head>
<meta charset="utf-8">
<title>Quiet Meadows at 41 Acres – Retirement Boarding Flyer</title>
<link href="https://fonts.googleapis.com/css2?family=Poppins:wght@400;500;600;700&display=swap" rel="stylesheet">
<style>
  :root {
    --orange: #EE7325;
    --orange-soft: #F08F49;
    --peach: #F5BC92;
    --cream: #FAE3D3;
    --ivory: #FDF4ED;
    --ink: #0d0d0d;
    --panel: rgba(12,12,12,0.82);
    --white: #ffffff;
    --leaf-deep: #2b3f1f;
    --leaf-dark: #1c2616;
  }
  * { box-sizing: border-box; margin: 0; padding: 0; }
  html, body { width: 961px; height: 1200px; overflow: hidden; }
  body {
    background: var(--cream);
    font-family: "Poppins", sans-serif;
    color: var(--white);
    position: relative;
  }
  .flyer {
    position: absolute; left: 55px; top: 0;
    width: 851px; height: 1200px;
    overflow: hidden; background: var(--ink);
  }
  .hero-photo {
    position: absolute; inset: 0 0 auto 0; height: 900px;
    background: linear-gradient(180deg, var(--leaf-deep) 0%, var(--leaf-dark) 45%, #141812 65%, var(--ink) 85%);
  }
  .title {
    position: absolute; left: 48px; top: 102px;
    font-size: 37px; font-weight: 700; letter-spacing: -0.3px; line-height: 1.2;
  }
  .subtitle {
    position: absolute; left: 48px; top: 193px;
    font-size: 29px; font-weight: 700; line-height: 40px; text-transform: uppercase;
  }
  .fees {
    position: absolute; left: 50px; top: 521px; width: 299px; height: 204px;
    background: var(--panel); border-radius: 8px; padding: 20px 0 0 34px;
  }
  .fees h2 {
    font-size: 21px; font-weight: 500; display: inline-block;
    padding: 0 20px 4px 0; border-bottom: 1.5px solid var(--white); width: 194px;
  }
  .fee-row { display: flex; margin-top: 13px; padding-left: 15px; height: 31px; align-items: center; }
  .fee-row:first-of-type { margin-top: 12px; }
  .fee-label { width: 116px; font-size: 17px; }
  .fee-label sub { font-size: 10px; vertical-align: baseline; }
  .fee-price { font-size: 19px; font-weight: 600; color: var(--orange); }
  .intro {
    position: absolute; left: 372px; top: 518px; width: 440px;
    font-size: 13.5px; line-height: 18.5px;
  }
  .features { position: absolute; left: 0; top: 0; }
  .feature { position: absolute; width: 120px; text-align: center; font-size: 14.5px; }
  .feature svg { display: block; margin: 0 auto 6px; width: 54px; height: 54px; }
  .contact-note {
    position: absolute; left: 48px; top: 1014px; display: flex; gap: 10px;
    font-size: 15.5px; line-height: 19px;
  }
  .call { position: absolute; left: 48px; top: 1069px; font-size: 20px; }
  .call strong { color: var(--orange); font-weight: 600; }
  .phone { position: absolute; left: 48px; top: 1102px; display: flex; align-items: center; gap: 10px; font-size: 20px; letter-spacing: 0.5px; }
  .gallery { position: absolute; left: 0; top: 0; width: 851px; height: 1200px; }
</style>
</head>
<body>
<main class="flyer">
  <div class="hero-photo" role="img" aria-label="Photo of a rider with her horse in a green outdoor setting"></div>

  <h1 class="title">Quiet Meadows at 41 Acres</h1>
  <p class="subtitle">Luxury Boarding<br>Stable for Retired<br>Horses</p>

  <section class="fees">
    <h2>Boarding Fees</h2>
    <div class="fee-row"><span class="fee-label">1<sub>st</sub> horse</span><span class="fee-price">$1,100/mo</span></div>
    <div class="fee-row"><span class="fee-label">2<sub>nd</sub> horse</span><span class="fee-price">$900/mo</span></div>
    <div class="fee-row"><span class="fee-label">3<sub>rd</sub> horse</span><span class="fee-price">$700/mo</span></div>
  </section>

  <p class="intro">Now available a premier retirement horse boarding facility, where luxury meets equestrian excellence! We have 6 available stalls, conveniently located in Summerfield, NC. Our facility offers top tier amenities where every detail is meticulously crafted to ensure quality care for your retired equine companions. From spacious stalls with back patios to lush pastures for gentle exercise, every detail is crafted to ensure well being. You have access to a world class riding arena with stadium lights, miles of trails through 41 acres, top quality feed and hay, and passionate, loving care from a staff with decades of experience.</p>

  <div class="features">
    <div class="feature" style="left:29px;top:776px">
      <svg viewBox="0 0 54 54" fill="none" stroke="#fff" stroke-width="1.8" stroke-linejoin="round"><path d="M14 12h22l8 10-19 24L6 22z"/><path d="M6 22h38M19 12l-4 10 10 24 10-24-4-10M25 12l-6 10M25 12l6 10"/><path d="M46 6l1.5 3 3 1.5-3 1.5L46 15l-1.5-3-3-1.5 3-1.5zM44 40l1 2 2 1-2 1-1 2-1-2-2-1 2-1z"/></svg>
      Luxurious</div>
    <div class="feature" style="left:157px;top:774px">
      <svg viewBox="0 0 54 54" fill="none" stroke="#fff" stroke-width="1.8"><path d="M27 3l5 4 6-1 2 6 6 3-1 6 4 5-4 5 1 6-6 3-2 6-6-1-5 4-5-4-6 1-2-6-6-3 1-6-4-5 4-5-1-6 6-3 2-6 6 1z"/><circle cx="27" cy="27" r="13"/><path d="M21 27l4 4 8-8" stroke-width="2.4"/></svg>
      Quality Facilities</div>
    <div class="feature" style="left:296px;top:776px">
      <svg viewBox="0 0 54 54" fill="none" stroke="#fff" stroke-width="1.8" stroke-linejoin="round"><path d="M27 31c-6-4-9-7-9-10a4 4 0 0 1 9-1 4 4 0 0 1 9 1c0 3-3 6-9 10z"/><path d="M6 34l8-6h8l6 3-2 3h-8M14 44l4-3h10l12-8M36 6l10 0v8M46 20l-8 6h-8l-6-3 2-3h8M40 10l-4 3H26L14 21"/></svg>
      Loving Care</div>
    <div class="feature" style="left:90px;top:873px">
      <svg viewBox="0 0 54 54" fill="none" stroke="#fff" stroke-width="2.2"><circle cx="27" cy="27" r="23"/><path d="M27 4v46M27 27L11 43M27 27l16 16"/></svg>
      Peaceful</div>
    <div class="feature" style="left:234px;top:873px">
      <svg viewBox="0 0 54 54" fill="none" stroke="#fff" stroke-width="1.8" stroke-linejoin="round"><path d="M27 46L8 27a10 10 0 0 1 19-12 10 10 0 0 1 19 12z"/><path d="M14 28l8-6 6 3 6-4 8 6M20 34l5 5M24 30l6 6M28 27l6 6"/></svg>
      Kind</div>
  </div>

  <div class="contact-note">
    <svg width="30" height="34" viewBox="0 0 30 34" fill="none" stroke="#fff" stroke-width="1.8"><path d="M13 32S3 21 3 13a10 10 0 0 1 20 0c0 2-.5 4-1.5 6"/><circle cx="13" cy="13" r="4"/><path d="M18 27l5-4 5 4v6h-10z"/></svg>
    <span>Contact us for a tour of Quiet<br>Meadows at 41 Acres</span>
  </div>
  <p class="call">Call or text <strong>Marisol</strong></p>
  <p class="phone">
    <svg width="34" height="34" viewBox="0 0 34 34" fill="none" stroke="#fff" stroke-width="1.6"><circle cx="17" cy="17" r="15.5"/><path d="M11 9l3 0 2 5-2 2c1 3 3 5 5 6l2-2 5 2v3c0 1-1 2-2 2-8 0-15-7-15-15 0-1 1-2 2-3z"/></svg>
    336-555-0147
  </p>

  <svg class="gallery" viewBox="0 0 851 1200">
    <defs>
      <linearGradient id="aerial-forest" x1="0" y1="0" x2="0" y2="1"><stop offset="0" stop-color="#3f7a22"/><stop offset="1" stop-color="#5c9a34"/></linearGradient>
      <linearGradient id="aerial-barn" x1="0" y1="0" x2="1" y2="1"><stop offset="0" stop-color="#4c8a2a"/><stop offset="1" stop-color="#9a978a"/></linearGradient>
      <linearGradient id="barn-aisle" x1="0" y1="0" x2="0" y2="1"><stop offset="0" stop-color="#8a6238"/><stop offset="1" stop-color="#5a3a1e"/></linearGradient>
    </defs>
    <circle cx="717" cy="858" r="133" fill="url(#aerial-forest)" stroke="var(--orange)" stroke-width="2" role="img" aria-label="Aerial photo of the forested property with riding arena"/>
    <circle cx="517" cy="984" r="141" fill="url(#aerial-barn)" stroke="var(--orange)" stroke-width="2" role="img" aria-label="Aerial photo of the barn, arena and driveway"/>
    <circle cx="718" cy="1076" r="137" fill="url(#barn-aisle)" stroke="var(--orange)" stroke-width="2" role="img" aria-label="Photo of the wooden barn aisle lined with stalls"/>
  </svg>
</main>
</body>
</html>
```